Tarek & Lubna's 50th Anniversary Celebration & Reunion

I need a flyer to send out via email and for posting on facebook to invite guests to a 50th wedding anniversary / family reunion.

Location is sunny La Jolla CA the Jewel of San Diego's Coast.

Week long daily activities starting Mon July 28-Aug 1st Friday, The event will be on Wednesday.
* Daily Catered Family Breakfast at the Marlow Hall of La Jolla
* Daily group activities including
*Exploring La Jolla Beaches & Ocean Cave Kayaking
*TideLand Private Behind the Scenes Tour
*World Famous Harbor Wild Park
*Sunset Balloon Ride
*Private Yatch on the Bay

Actual Anniversary event will take place Thursday December 28, 2013 at 5pm at the Marlow Hall.

There are many local hotels around the Marlow Hall. 4512 Pell Ave, La Jolla, CA 92037

Host is Remond and the entire Halabi Family. For questions, please email Remond@thegrovefeasts.com

Target Market(s)

all ages from 10 year olds to 70 year olds. Should appeal to all

Industry/Entity Type

Wedding

Font styles to use
Script

Colors

Designer to choose colors to be used in the design.

Requirements
Must have
• Fun graphics, including one with a stretch limo as there will be one available

Nice to have
• Logo for TideLand Inserting a picture of an actual wedding 50 years ago or so of the bride and groom. incorporating the limo cropped out of the picture attached would also be nice

```html
<!DOCTYPE html>
<html lang="en">
<head>
<meta charset="utf-8">
<title>Tarek &amp; Lubna's 50th Anniversary Celebration &amp; Reunion</title>
<link rel="stylesheet" href="https://fonts.googleapis.com/css2?family=Great+Vibes&family=Raleway:wght@200;300&family=Roboto+Condensed:wght@400;700&display=swap">
<style>
:root{
  --stage:#3a3a3a;
  --paper:#ffffff;
  --mist:#e6ebf3;
  --leaf:#8cc63f;
  --ink:#111111;
  --soft-ink:#222222;
  --ghost:#b9bcc2;
  --bark:#2b2220;
}
*{margin:0;padding:0;box-sizing:border-box}
html,body{width:1200px;height:1000px;overflow:hidden}
body{background:var(--stage);position:relative;font-family:"Roboto Condensed",sans-serif;color:var(--ink)}
.flyer{position:absolute;left:295px;top:90px;width:610px;height:815px;background:var(--paper);overflow:hidden}
.sky{position:absolute;left:0;top:0;width:610px;height:360px}
.abs{position:absolute}
.title{left:18px;top:22px;font-family:"Great Vibes",cursive;font-size:82px;line-height:1;white-space:nowrap}
.title .amp{color:var(--ghost);font-size:60px;margin:0 -6px}
.branch-top{left:300px;top:0;width:310px;height:195px;border-radius:4px;
  background:radial-gradient(ellipse at 70% 40%,rgba(43,34,32,.28),rgba(140,198,63,.18) 55%,rgba(230,235,243,0) 80%)}
.wedding-photo{left:22px;top:134px;width:172px;height:206px;background:var(--paper);padding:8px;transform:rotate(-5deg);box-shadow:0 2px 6px rgba(0,0,0,.35)}
.wedding-photo div{width:100%;height:100%;background:linear-gradient(160deg,#8b8b8b,#3c3c3c 55%,#d8d8d8)}
.fifty{left:190px;top:180px;font-family:"Raleway",sans-serif;font-weight:200;font-size:142px;line-height:1;letter-spacing:-4px}
.fifty sup{font-size:30px;font-weight:300;vertical-align:top;position:relative;top:18px;letter-spacing:0;margin-left:4px}
.occasion{left:358px;top:212px;font-family:"Great Vibes",cursive;font-size:29px;line-height:1.2;white-space:nowrap}
.occasion span{display:block;margin-left:-8px}
.location{left:0;top:368px;width:405px;height:54px;background:linear-gradient(90deg,var(--mist) 55%,rgba(230,235,243,0));padding:5px 0 0 33px}
.location h2{font-family:"Raleway",sans-serif;font-weight:300;font-size:21px;line-height:1.1}
.location p{font-weight:700;font-size:15.5px;margin-top:2px}
.week{left:31px;top:430px;font-size:12px;line-height:1.4}
.activities{left:0;top:471px;width:405px;height:110px;background:linear-gradient(90deg,var(--mist) 40%,rgba(230,235,243,0));padding:3px 0 0 33px;list-style:none;font-size:12px;line-height:15px}
.activities li::before{content:"\2022";margin-right:5px}
.date-card{left:420px;top:364px;width:146px;height:181px;border:2px solid var(--ink);border-radius:9px;background:var(--paper);text-align:center;overflow:hidden}
.date-card .month{font-weight:700;font-size:25px;line-height:1;margin-top:7px}
.date-card .weekday{background:var(--mist);color:var(--leaf);font-family:"Raleway",sans-serif;font-weight:300;font-size:15px;letter-spacing:2px;margin-top:5px;padding:3px 0}
.date-card .day{background:var(--mist);color:var(--leaf);font-weight:700;font-size:72px;line-height:70px;padding-bottom:2px}
.date-card .day sup{font-size:26px;vertical-align:top;position:relative;top:-2px}
.date-card .time{font-weight:700;font-size:33px;line-height:1;margin-top:6px}
.details{left:24px;top:592px;font-size:12px;line-height:18px}
.details b{font-weight:700}
.host{left:265px;top:643px;width:345px;height:54px;background:var(--leaf);border-radius:9px 0 0 9px;text-align:right;padding:8px 38px 0 0;font-size:12px;line-height:16px;color:var(--soft-ink)}
.branch-bottom{left:0;top:655px;width:245px;height:160px;background:radial-gradient(ellipse at 20% 70%,rgba(43,34,32,.3),rgba(140,198,63,.18) 55%,rgba(255,255,255,0) 80%)}
.limo-photo{left:215px;top:705px;width:395px;height:110px;background:linear-gradient(180deg,rgba(200,212,205,0) 0%,#b7c4b0 35%,#1d1d1d 62%,#262626 80%,#9a9a92 100%)}
</style>
</head>
<body>
<main class="flyer">
  <svg class="abs sky" viewBox="0 0 610 360" aria-hidden="true">
    <path d="M0 0H610V238C470 300 330 340 190 336C110 333 45 280 0 218Z" fill="var(--mist)"/>
    <path d="M0 218C45 280 110 333 190 336C330 340 470 300 610 238" fill="none" stroke="var(--leaf)" stroke-width="4"/>
  </svg>
  <div class="abs branch-top" role="img" aria-label="Tree branch with green leaves, two love birds and small red hearts"></div>
  <h1 class="abs title">Tarek<span class="amp">&amp;</span>Lubna's</h1>
  <figure class="abs wedding-photo"><div role="img" aria-label="Black and white wedding photo of the couple fifty years ago"></div></figure>
  <div class="abs fifty">50<sup>th</sup></div>
  <p class="abs occasion">Anniversary Celebration<span>&amp; Reunion</span></p>

  <section class="abs location">
    <h2>Location</h2>
    <p>Sunny La Jolla CA the Jewel of San Diego's Coast</p>
  </section>
  <p class="abs week">Week long daily activities starting Mon July 28-Aug 1st Friday,<br>The event will be on Wednesday.</p>
  <ul class="abs activities">
    <li>Daily Catered Family Breakfast at the Marlow Hall of La Jolla</li>
    <li>Daily group activities including</li>
    <li>Exploring La Jolla Beaches &amp; Ocean Cave Kayaking</li>
    <li>TideLand Private Behind the Scenes Tour</li>
    <li>World Famous Harbor Wild Park</li>
    <li>Sunset Balloon Ride</li>
    <li>Private Yatch on the Bay</li>
  </ul>

  <div class="abs date-card">
    <div class="month">JULY</div>
    <div class="weekday">WEDNESDAY</div>
    <div class="day">28<sup>TH</sup></div>
    <div class="time">5:00PM</div>
  </div>

  <p class="abs details">Actual Anniversary event will take place <b>Thursday December 28, 2013 at 5pm at the Marlow Hall.</b><br>
  There are many local hotels around <b>The Marlow Hall. 4512 Pell Ave, La Jolla, CA 92037</b></p>

  <div class="abs branch-bottom" role="img" aria-label="Bare tree branch with green leaves"></div>
  <div class="abs limo-photo" role="img" aria-label="Black stretch limousine parked in front of palm trees"></div>
  <p class="abs host">Host is Remond and the entire Halabi Family.<br>For questions, please email Remond@thegrovefeasts.com</p>
</main>
</body>
</html>
```